Business Coach needs an elegant business card design

I need a business card design based around my logo for color and to look like a millionaire dollar coach. Incorporate the color of my logo with something creative and attractive that stands out. I am focused on high end companies and the card must look and feel that way.

Target Market(s)

High End Companies and Business Owners - Training People to become millionaires

Industry/Entity Type

Business

Requirements
Must have
• Front -
Logo (attached file) - Website (marlowkeeve.com) - Name (Marlow Keeve) Phone (555.201.7746) - Email (marlow@marlowkeeve.com) (My Title - Success Coach)
Back -
Slogan - Vision (see it) . Action (do it) . Transformation (be it)
Website - Learn More @ marlowkeeve.com

Creative High End Look!
Nice to have
Should not have
• Cheap standard look
nothing traditional

```html
<!DOCTYPE html>
<html lang="en">
<head>
<meta charset="UTF-8">
<title>Marlow Keeve Coaching – Business Card</title>
<link href="https://fonts.googleapis.com/css2?family=Open+Sans:wght@400;600;700&display=swap" rel="stylesheet">
<style>
  :root {
    --backdrop: #e9e9e9;
    --card: #1c1b1b;
    --ink: #f2f2f2;
    --ink-soft: #b9b9b9;
    --ghost: #222121;
    --ghost-line: #2e2d2d;
    --rule: #8a8a8a;
  }
  * { margin: 0; padding: 0; box-sizing: border-box; }
  html, body {
    width: 1200px; height: 675px; overflow: hidden;
    background: var(--backdrop);
    font-family: "Open Sans", Arial, sans-serif;
  }
  .stage {
    position: relative; width: 1200px; height: 675px;
    display: flex; align-items: center; justify-content: center; gap: 50px;
  }
  .card {
    position: relative; width: 520px; height: 297px;
    background: var(--card); color: var(--ink); overflow: hidden;
    box-shadow: 0 6px 18px rgba(0,0,0,.18);
  }
  .ghost-ring {
    position: absolute; border-radius: 50%;
    border: 10px solid var(--ghost-line); background: var(--ghost);
  }
  .card-front .ghost-ring { width: 170px; height: 170px; left: 50px; top: 112px; }
  .card-back .ghost-ring  { width: 210px; height: 210px; left: 155px; top: 44px; }

  .brand {
    position: absolute; left: 30px; top: 44px;
    display: flex; align-items: center; gap: 12px;
  }
  .brand-dot { width: 44px; height: 44px; border-radius: 50%; background: var(--ink); flex: none; }
  .brand-name {
    font-weight: 600; font-size: 16px; letter-spacing: 2px;
    text-transform: uppercase; line-height: 1.3; color: var(--ink);
  }
  .brand-rule {
    position: absolute; left: 272px; right: 0; top: 100px;
    height: 1px; background: var(--rule);
  }
  .contact { position: absolute; left: 290px; top: 112px; }
  .contact-name { font-weight: 700; font-size: 14px; line-height: 18px; }
  .contact-title { font-size: 9px; color: var(--ink-soft); margin-bottom: 8px; }
  .contact-list { list-style: none; }
  .contact-list li {
    display: flex; align-items: center; gap: 12px;
    font-size: 12px; line-height: 19px; white-space: nowrap;
  }
  .contact-list svg { width: 12px; height: 12px; fill: var(--ink); flex: none; }

  .slogan {
    position: absolute; left: 0; right: 0; top: 102px;
    text-align: center; font-size: 14px; line-height: 21px; color: var(--ink);
  }
  .slogan strong { font-weight: 700; }
  .learn-more {
    position: absolute; left: 0; right: 0; top: 182px;
    text-align: center; font-size: 11px; color: var(--ink);
  }
  .learn-more strong { font-weight: 700; }
</style>
</head>
<body>
<main class="stage">
  <section class="card card-front" aria-label="Card front">
    <div class="ghost-ring" aria-hidden="true"></div>
    <div class="brand">
      <span class="brand-dot" aria-hidden="true"></span>
      <span class="brand-name">Marlow Keeve<br>Coaching</span>
    </div>
    <div class="brand-rule"></div>
    <div class="contact">
      <p class="contact-name">Marlow Keeve</p>
      <p class="contact-title">Success Coach</p>
      <ul class="contact-list">
        <li>
          <svg viewBox="0 0 24 24" aria-hidden="true"><path d="M6.6 10.8a15 15 0 0 0 6.6 6.6l2.2-2.2c.3-.3.7-.4 1-.2 1.1.4 2.3.6 3.6.6.6 0 1 .4 1 1V20c0 .6-.4 1-1 1C10.6 21 3 13.4 3 4c0-.6.4-1 1-1h3.5c.6 0 1 .4 1 1 0 1.3.2 2.5.6 3.6.1.3 0 .7-.2 1z"/></svg>
          555.201.7746
        </li>
        <li>
          <svg viewBox="0 0 24 24" aria-hidden="true"><path d="M2 5h20v14H2zm2 2v.5l8 5 8-5V7zm0 2.8V17h16V9.8l-8 5z"/></svg>
          marlow@marlowkeeve.com
        </li>
        <li>
          <svg viewBox="0 0 24 24" aria-hidden="true"><path d="M12 2a10 10 0 1 0 0 20 10 10 0 0 0 0-20zm6.9 9h-3a15 15 0 0 0-1.2-5.3A8 8 0 0 1 18.9 11zM12 4.1c.9 1.3 1.7 3.6 1.9 6.9h-3.8c.2-3.3 1-5.6 1.9-6.9zM9.3 5.7A15 15 0 0 0 8.1 11h-3a8 8 0 0 1 4.2-5.3zM5.1 13h3a15 15 0 0 0 1.2 5.3A8 8 0 0 1 5.1 13zm6.9 6.9c-.9-1.3-1.7-3.6-1.9-6.9h3.8c-.2 3.3-1 5.6-1.9 6.9zm2.7-1.6a15 15 0 0 0 1.2-5.3h3a8 8 0 0 1-4.2 5.3z"/></svg>
          www.marlowkeeve.com
        </li>
      </ul>
    </div>
  </section>

  <section class="card card-back" aria-label="Card back">
    <div class="ghost-ring" aria-hidden="true"></div>
    <p class="slogan">
      <strong>VISION.</strong> Picture Where You Go<br>
      <strong>ACTION.</strong> Commit To Each Step<br>
      <strong>TRANSFORMATION.</strong> Become Who You Chose!
    </p>
    <p class="learn-more"><strong>Learn More:</strong> www.marlowkeeve.com</p>
  </section>
</main>
</body>
</html>
```